Morvik Construction Business Card

I need a business card design for my company.
We are a construction/machinery company.
I would like to see my logo on the front of the card and my details on the other side
I would like the card to be black or dark grey in colour,with my logo as i send it or modified with a lighter blue colour
I would like to see the design kept fairly simple,but eye catching at the same time
Industry/Entity Type
Business
Colors
00a990
1b1b1b
000000
474747
ececec

```html
<!DOCTYPE html>
<html lang="en">
<head>
<meta charset="utf-8">
<title>Morvik Construction Business Card</title>
<link rel="stylesheet" href="https://fonts.googleapis.com/css2?family=Roboto:wght@400;500;700&display=swap">
<style>
  :root {
    --stage: #3c3c3c;
    --ink-black: #000000;
    --ink-dark: #1b1b1b;
    --ink-grey: #474747;
    --swoosh: #a9a9a9;
    --paper: #f7f7f7;
    --white: #ffffff;
  }
  * { margin: 0; padding: 0; box-sizing: border-box; }
  html, body {
    width: 1105px; height: 1200px; overflow: hidden;
    background: var(--stage);
    font-family: "Roboto", Arial, sans-serif;
  }
  .card {
    position: absolute; left: 196px; width: 720px; height: 412px;
    overflow: hidden; background: var(--ink-black);
  }
  .card--front { top: 146px; }
  .card--back { top: 602px; }
  .card__wave { position: absolute; inset: 0; width: 720px; height: 412px; }

  .brand {
    position: absolute; left: 0; right: 0; text-align: center;
    color: var(--white); font-weight: 700; text-transform: uppercase; line-height: 1;
  }
  .brand__name { display: block; }
  .brand__sub { display: block; }
  .card--front .brand { top: 48px; }
  .card--front .brand__name { font-size: 50px; letter-spacing: 3px; }
  .card--front .brand__sub { font-size: 22px; letter-spacing: 5px; margin-top: 8px; }

  .card--back .brand { top: 175px; left: -28px; }
  .card--back .brand__name { font-size: 56px; letter-spacing: 4px; }
  .card--back .brand__sub { font-size: 25px; letter-spacing: 6px; margin-top: 10px; }

  .contact {
    position: absolute; left: 0; right: 0; top: 292px;
    text-align: center; color: var(--ink-dark);
  }
  .contact__name { font-size: 23px; font-weight: 500; letter-spacing: 0.5px; }
  .contact__role { font-size: 19px; font-weight: 500; }
  .contact__line {
    display: flex; justify-content: center; align-items: center; gap: 8px;
    margin-top: 12px; font-size: 17px; font-weight: 500;
  }
  .contact__line svg { width: 17px; height: 17px; fill: var(--ink-dark); }
  .contact__address { margin-top: 12px; font-size: 18px; font-weight: 500; }
</style>
</head>
<body>

<section class="card card--front">
  <svg class="card__wave" viewBox="0 0 720 412" aria-hidden="true">
    <path d="M0 178 Q 260 250 720 252 L720 262 Q 300 262 0 196 Z" fill="var(--swoosh)"/>
    <path d="M0 198 Q 300 262 720 258 L720 412 L0 412 Z" fill="var(--paper)"/>
    <path d="M0 198 Q 300 262 720 258" fill="none" stroke="var(--ink-black)" stroke-width="3"/>
  </svg>
  <div class="brand">
    <span class="brand__name">Morvik</span>
    <span class="brand__sub">Construction</span>
  </div>
  <div class="contact">
    <p><span class="contact__name">DANIEL REYES</span> <span class="contact__role">- CEO/FOUNDER</span></p>
    <p class="contact__line">
      <svg viewBox="0 0 24 24" aria-hidden="true"><path d="M6.6 10.8a15.1 15.1 0 0 0 6.6 6.6l2.2-2.2c.3-.3.7-.4 1-.2 1.1.4 2.3.6 3.6.6.6 0 1 .4 1 1V20c0 .6-.4 1-1 1A17 17 0 0 1 3 4c0-.6.4-1 1-1h3.5c.6 0 1 .4 1 1 0 1.3.2 2.5.6 3.6.1.3 0 .7-.2 1z"/></svg>
      <span>555 210 4873</span>
      <svg viewBox="0 0 24 24" aria-hidden="true"><path d="M3 5h18v14H3z M4 6.5v.3l8 5.5 8-5.5v-.3z" fill-rule="evenodd"/></svg>
      <span>daniel@morvikbuild.com</span>
    </p>
    <p class="contact__address">214 Alder Ridge Road, Fairbanks, Alaska 99701</p>
  </div>
</section>

<section class="card card--back">
  <div class="brand">
    <span class="brand__name">Morvik</span>
    <span class="brand__sub">Construction</span>
  </div>
</section>

</body>
</html>
```